Business Card Design Project

I would like to have a project of business card with incorporated attachted logo elements in warm colors like: gold, yellow, brown.
We would like incorporate below information into the design
Name of the Company: Continental Hoop Invitational
Name: Dorian Pelkey
Position: Project Director
e-mail: dorian@hoopinvitational.net
mobile: +65 83147092
website: www.hoopinvitational.net
Address: 47 Marbury Lane, #06-11, Singapore 915274
There is a picture attachted which can be used as a back side of the buisness card - we would like to follow the colors theme on the front card ( with the person contact details) how ever the front card we will prefer with white background but with graphfic elements coming from logo.
Project Deadline Extended
Reason: the project has been launched on 24 of April with deadline by 24 of April by mistakes. Thats why I would like to extend the deadline.
Name: Dorian Pelkey
mobile: +65 83147092

```html
<!DOCTYPE html>
<html lang="en">
<head>
<meta charset="utf-8">
<title>Dorian Pelkey – Business Card</title>
<link href="https://fonts.googleapis.com/css2?family=Noto+Sans:ital,wght@0,400;0,700;1,400&display=swap" rel="stylesheet">
<style>
  :root {
    --page: #ffffff;
    --card: #ffffff;
    --card-border: #222222;
    --orange-deep: #f7941d;
    --orange-light: #fec52e;
    --purple: #6b1d87;
    --purple-deep: #5a1a80;
    --magenta: #a3137c;
    --brand-purple: #6b2790;
    --label: #dccbe8;
    --ink: #222222;
    --ink-soft: #333333;
    --title-grey: #6a6a6a;
  }
  * { margin: 0; padding: 0; box-sizing: border-box; }
  html, body {
    width: 1200px; height: 900px; overflow: hidden;
    background: var(--page);
    font-family: "Noto Sans", Verdana, sans-serif;
  }
  .card {
    position: absolute; left: 67px; top: 135px;
    width: 1052px; height: 603px;
    background: var(--card);
    border: 1px solid var(--card-border);
    overflow: hidden;
  }
  .card-art { position: absolute; inset: 0; width: 100%; height: 100%; }
  .brand {
    position: absolute; left: 40px; top: 100px;
    display: flex; align-items: center; gap: 22px;
  }
  .brand-dot {
    width: 64px; height: 64px; border-radius: 50%;
    background: var(--brand-purple); flex: none;
  }
  .brand-name {
    color: var(--brand-purple);
    font-weight: 700; font-size: 38px; line-height: 1.15;
    text-transform: uppercase; letter-spacing: 0.5px;
  }
  .website {
    position: absolute; left: 25px; top: 338px;
    color: var(--brand-purple); font-size: 31px;
  }
  .person-name {
    position: absolute; left: 568px; top: 170px;
    font-size: 62px; color: var(--ink); font-weight: 400;
  }
  .person-title {
    position: absolute; left: 644px; top: 246px;
    font-size: 40px; font-style: italic; color: var(--title-grey);
  }
  .contacts {
    position: absolute; left: 300px; top: 439px;
    display: grid; grid-template-columns: 200px auto;
    row-gap: 10px; column-gap: 8px;
    font-size: 24px; line-height: 36px;
  }
  .contact-label { color: var(--label); text-align: right; }
  .contact-value { color: var(--ink-soft); white-space: nowrap; }
  .contact-value.indent { padding-left: 30px; }
  .contact-value.indent-sm { padding-left: 20px; }
</style>
</head>
<body>
  <div class="card">
    <svg class="card-art" viewBox="0 0 1052 603" preserveAspectRatio="none" aria-hidden="true">
      <defs>
        <linearGradient id="warm" x1="0" y1="0" x2="1" y2="0">
          <stop offset="0" stop-color="var(--orange-deep)"/>
          <stop offset="1" stop-color="var(--orange-light)"/>
        </linearGradient>
        <linearGradient id="wave" x1="0" y1="0" x2="0.3" y2="1">
          <stop offset="0" stop-color="var(--purple)"/>
          <stop offset="0.6" stop-color="var(--purple-deep)"/>
          <stop offset="1" stop-color="var(--magenta)"/>
        </linearGradient>
      </defs>
      <path d="M0 0 H451 C470 120 445 260 420 360 C395 460 340 540 305 603 H0 Z" fill="url(#warm)"/>
      <path d="M451 0 H491 C505 120 525 250 522 330 C520 420 500 520 488 603 H305 C340 540 395 460 420 360 C445 260 470 120 451 0 Z" fill="url(#wave)"/>
    </svg>

    <div class="brand">
      <span class="brand-dot"></span>
      <div class="brand-name">Continental<br>Hoop<br>Invitational</div>
    </div>

    <div class="website">www.hoopinvitational.net</div>

    <h1 class="person-name">Dorian Pelkey</h1>
    <p class="person-title">Project Director</p>

    <div class="contacts">
      <span class="contact-label">e-mail:</span>
      <span class="contact-value indent">dorian@hoopinvitational.net</span>
      <span class="contact-label">mobile:</span>
      <span class="contact-value indent-sm">+65 83147092</span>
      <span class="contact-label">Address:</span>
      <span class="contact-value">47 Marbury Lane, #06-11, Singapore 915274</span>
    </div>
  </div>
</body>
</html>
```